Fresh & Clean *NEW* BUSINESS CARD Needed - OPTOMETRY Clinic/Optical

High-tech optometry practice with 3 doctors seeking new business card.  We provide eye exams, sell, designer glasses/contacts/specialty eyewear and treat ocular diseases.  For our business cards, we are seeking fresh, clean, and crisp design as we grow our team (staffing change).  Simply adding doctors is making the card look busy/cluttered.
 Looking for professional, less cluttered look yet still have our logo, doctor names, phone, address, and website....If possible!  :)
Names:
Marcia Trelford, O.D.
Ned Pallister, O.D.
Oona Ferrant, O.D.
Phone: 555-014-2738
Website: www.BrightLensHub.example
Address:  417 Garnet R. Holloway, Harrowmere, QX 00000
Ultimately we have the main business card with all doctor sames and that card has two versions  (front is always the same).  The back has two designs (1) displays next appointment time/date, (2) for "general use" (non-appointment.)    I have attached what we have used in the past.  
We also need a design template for each team member in our practice with their name, title, and email.   Those should be designed with the "general use" back (see attached).
**Open to entirely new design so don't feel obligated to keep current format.  Need new perspective!  Also including our watermark and some other design features we have consistently used in past in our portfolio.  Included are two options for logos--vertical and horizontal.
**I also would like to remove "Member of Sight Alliance" on our logo if possible**
 Other image files available upon request.

Target Market(s)

New patient & Current Patients

Industry/Entity Type

Optometry

Contact Information for Business Card

High-tech optometry practice with 3 doctors seeking new business card.  We provide eye exams, sell, designer glasses/contacts/specialty eyewear and treat ocular diseases.  For our business cards, we are seeking fresh, clean, and crisp design as we grow our team (staffing change).  Simply adding doctors is making the card look busy/cluttered.  Looking for professional, less cluttered look yet still have our logo, doctor names, phone, address, and website....If possible!  :) Names: Marcia Trelford, O.D. Ned Pallister, O.D. Oona Ferrant, O.D. Phone: 555-014-2738 Website: www.BrightLensHub.example Address:  417 Garnet R. Holloway, Harrowmere, QX 00000 Ultimately we have the main business card with all doctor sames and that card has two versions  (front is always the same).  The back has two designs (1) displays next appointment time/date, (2) for "general use" (non-appointment.)    I have attached what we have used in the past.   We also need a design template for each team member in our practice with their name, title, and email.   Those should be designed with the "general use" back (see attached). **Open to entirely new design so don't feel obligated to keep current format.  Need new perspective!  Also including our watermark and some other design features we have consistently used in past in our portfolio.  Included are two options for logos--vertical and horizontal. **I also would like to remove "Member of Sight Alliance" on our logo if possible**  Other image files available upon request.

Font styles to use
Other font styles liked:
• We have used Montserrat / Yellowtail in the past

Colors

Designer to choose colors to be used in the design.

Requirements
Must have
• Clean & Fresh Design with Logo / Info provided in description. Horizontal orientation. **I have included the CMYK colors we currently have in our logo.
Should not have
• Cluttered

```html
<!DOCTYPE html>
<html lang="en">
<head>
<meta charset="UTF-8">
<title>Bright Lens Hub – Business Card</title>
<link rel="stylesheet" href="https://fonts.googleapis.com/css2?family=Montserrat:wght@400;500;600&family=Great+Vibes&display=swap">
<style>
  :root {
    --backdrop: #c8c8c8;
    --card: #ffffff;
    --ink: #6d6e71;
    --ink-soft: #9a9b9e;
    --rule: #8d8e91;
    --gold: #d9b00f;
    --ghost: #f3f4f6;
  }
  * { box-sizing: border-box; margin: 0; padding: 0; }
  html, body { width: 1200px; height: 900px; overflow: hidden; }
  body {
    background: var(--backdrop);
    font-family: "Montserrat", sans-serif;
    color: var(--ink);
    display: flex;
    flex-direction: column;
    align-items: center;
    justify-content: center;
    gap: 44px;
  }
  .card {
    position: relative;
    width: 560px;
    height: 320px;
    background: var(--card);
    border-radius: 26px;
    overflow: hidden;
    box-shadow: 0 6px 14px rgba(0,0,0,.18);
  }

  /* Appointment side */
  .appointment-title {
    position: absolute;
    top: 34px; left: 0; right: 0;
    text-align: center;
    font-family: "Great Vibes", cursive;
    font-size: 50px;
    font-weight: 400;
    color: var(--ink);
  }
  .appointment-title .accent { color: var(--gold); }
  .field-row {
    position: absolute;
    left: 70px; right: 70px;
    display: flex;
    gap: 30px;
  }
  .field-row.first { top: 138px; }
  .field-row.second { top: 186px; }
  .field {
    flex: 1;
    border-bottom: 1px solid var(--rule);
    height: 30px;
    display: flex;
    align-items: flex-end;
    justify-content: space-between;
    padding-bottom: 3px;
    font-size: 10px;
    letter-spacing: .08em;
    color: var(--ink-soft);
  }
  .notice {
    position: absolute;
    bottom: 34px; left: 0; right: 0;
    text-align: center;
    font-size: 11.5px;
    letter-spacing: .03em;
    color: var(--ink);
  }

  /* Practice side */
  .brand {
    position: absolute;
    top: 44px; left: 40px;
    display: flex;
    align-items: center;
    gap: 14px;
  }
  .brand-dot {
    width: 44px; height: 44px;
    border-radius: 50%;
    background: #8cc5d3;
  }
  .brand-name {
    font-size: 34px;
    font-weight: 400;
    letter-spacing: .02em;
    color: var(--ink);
  }
  .doctors {
    position: absolute;
    top: 128px; left: 40px;
    list-style: none;
    font-size: 21px;
    font-weight: 600;
    line-height: 1.3;
    color: var(--ink);
  }
  .doctors .title { color: var(--gold); font-weight: 500; }
  .contact {
    position: absolute;
    bottom: 30px; left: 40px;
    list-style: none;
    font-size: 15px;
    line-height: 1.6;
    color: var(--ink);
  }
  .contact li { display: flex; align-items: center; gap: 9px; }
  .contact svg { width: 18px; height: 18px; flex: none; }
  .address {
    position: absolute;
    right: 36px; bottom: 78px;
    text-align: right;
    font-size: 14px;
    line-height: 1.45;
    color: var(--ink);
  }
</style>
</head>
<body>

  <section class="card appointment-card">
    <h1 class="appointment-title">Appointment <span class="accent">Reminder</span></h1>
    <div class="field-row first">
      <div class="field"><span>NAME</span></div>
    </div>
    <div class="field-row second">
      <div class="field"><span>DATE</span></div>
      <div class="field"><span>TIME</span><span>AM/PM</span></div>
    </div>
    <p class="notice">If you unable to keep your appointment, kindly give us 24 hours notice</p>
  </section>

  <section class="card practice-card">
    <div class="brand">
      <span class="brand-dot"></span>
      <span class="brand-name">brightlenshub</span>
    </div>

    <ul class="doctors">
      <li>Marcia Trelford, <span class="title">O.D.</span></li>
      <li>Ned Pallister, <span class="title">O.D.</span></li>
      <li>Oona Ferrant, <span class="title">O.D.</span></li>
    </ul>

    <ul class="contact">
      <li>
        <svg viewBox="0 0 20 20" aria-hidden="true">
          <circle cx="10" cy="10" r="10" fill="var(--gold)"/>
          <path d="M7 5.5l1.6 2.4-1 1.1a6 6 0 0 0 3.4 3.4l1.1-1 2.4 1.6-.8 1.6c-3.8.2-7.7-3.7-7.5-7.5z" fill="#fff"/>
        </svg>
        <span>555-014-2738</span>
      </li>
      <li>
        <svg viewBox="0 0 20 20" aria-hidden="true">
          <circle cx="10" cy="10" r="10" fill="var(--gold)"/>
          <circle cx="10" cy="10" r="5" fill="none" stroke="#fff" stroke-width="1.2"/>
          <ellipse cx="10" cy="10" rx="2.2" ry="5" fill="none" stroke="#fff" stroke-width="1.1"/>
          <path d="M5 10h10" stroke="#fff" stroke-width="1.1"/>
        </svg>
        <span>www.BrightLensHub.example</span>
      </li>
    </ul>

    <p class="address">417 Garnet R. Holloway, Harrowmere<br>QX 00000</p>
  </section>

</body>
</html>
```